Church Lanterns Over Millbrook Gospel Booklet Design

We need a booklet designed that we will be printing to hand out in our community. Wording for each page will be provided and we need graphic design to produce the layouts in a format ready for print. Booklet will be 4.75" x 4.75" square and a total of 12 pages: 1 cover page front, 1 cover page back, 10 inside pages some of which will be full spread across 2 pages.

Target Market(s)

English speaking Westerners

Industry/Entity Type

Religious

Font styles to use
Serif

Colors
ffffff
85abd2
0292cd
33b8a4
5c5c5c

Requirements
Must have
• Minimalist design with clean look described in attached document
Nice to have
• Aesthetically pleasing graphics, crisp fonts, excellent turn around times
Should not have
• Effeminate design, busy look with too much graphic and text

```html
<!DOCTYPE html>
<html lang="en">
<head>
<meta charset="utf-8">
<title>Lanterns Over Millbrook – Gospel Booklet</title>
<link rel="stylesheet" href="https://fonts.googleapis.com/css2?family=Lora:ital,wght@0,400;0,600;0,700;1,400;1,600&family=Playfair+Display:ital,wght@0,700;1,600&display=swap">
<style>
  :root {
    --stage: #8c8e92;
    --white: #ffffff;
    --sky: #85abd2;
    --blue: #0292cd;
    --teal: #33b8a4;
    --ink: #5c5c5c;
    --deep: #0b3f63;
    --paper: #ffffff;
    --paper-edge: #e6edf3;
  }
  * { margin: 0; padding: 0; box-sizing: border-box; }
  html, body { width: 1200px; height: 1200px; overflow: hidden; }
  body {
    background: var(--stage);
    font-family: "Lora", serif;
    position: relative;
  }
  .page {
    position: absolute;
    overflow: hidden;
    box-shadow: 0 8px 22px rgba(0,0,0,.22);
  }

  /* Covers: square pages */
  .cover-front { left: 140px; top: 50px; width: 440px; height: 440px; }
  .cover-back  { left: 620px; top: 50px; width: 440px; height: 440px; }

  .cover-photo {
    position: absolute; inset: 0;
    background:
      radial-gradient(ellipse 60% 38% at 45% 78%, rgba(255,255,255,.75), rgba(133,171,210,.55) 45%, transparent 75%),
      linear-gradient(180deg, var(--deep) 0%, var(--blue) 45%, var(--sky) 70%, var(--teal) 100%);
  }
  .cover-back .cover-photo {
    background:
      radial-gradient(ellipse 50% 35% at 78% 55%, rgba(255,255,255,.7), rgba(133,171,210,.5) 45%, transparent 75%),
      linear-gradient(180deg, var(--deep) 0%, var(--blue) 50%, var(--sky) 68%, var(--deep) 100%);
  }

  .cover-title {
    position: absolute; left: 34px; top: 118px; width: 372px;
    font-family: "Playfair Display", serif;
    font-style: italic; font-weight: 600;
    font-size: 46px; line-height: 1.1;
    color: var(--white);
    transform: rotate(-10deg);
    transform-origin: left top;
    text-shadow: 0 2px 6px rgba(0,0,0,.25);
  }

  .church-info {
    position: absolute; left: 36px; top: 110px; width: 260px;
    color: var(--white);
  }
  .church-info h2 {
    font-weight: 700; font-size: 18px; letter-spacing: 1px; margin-bottom: 10px;
  }
  .church-info p { font-size: 13px; line-height: 1.55; }

  /* Inside spread: two square pages */
  .spread { left: 80px; top: 550px; width: 1040px; height: 520px; }
  .spread-photo {
    position: absolute; left: 0; top: 0; width: 520px; height: 520px;
    background:
      radial-gradient(ellipse 30% 55% at 78% 45%, rgba(255,255,255,.85), rgba(133,171,210,.5) 40%, transparent 72%),
      radial-gradient(ellipse 40% 45% at 22% 28%, rgba(51,184,164,.55), transparent 70%),
      linear-gradient(160deg, var(--sky) 0%, var(--blue) 45%, var(--deep) 100%);
  }
  .spread-text {
    position: absolute; left: 520px; top: 0; width: 520px; height: 520px;
    background: radial-gradient(ellipse 75% 65% at 55% 45%, var(--paper), var(--paper-edge) 100%);
    padding: 90px 36px 0 44px;
    text-align: right;
    color: var(--ink);
  }
  .intro { font-size: 17px; font-weight: 600; line-height: 1.45; }
  .quote-mark {
    font-family: "Playfair Display", serif; font-weight: 700;
    color: var(--blue); font-size: 64px; line-height: 1;
    text-align: center; height: 40px; margin: 24px 0 12px;
  }
  .verse { font-size: 24px; font-weight: 600; line-height: 1.35; }
  .reference {
    text-align: center; color: var(--teal);
    font-size: 20px; font-weight: 700; margin-top: 22px;
  }
</style>
</head>
<body>

  <section class="page cover-front">
    <div class="cover-photo" role="img" aria-label="Photo of three wooden crosses on a hill against a sunset sky"></div>
    <h1 class="cover-title">Lanterns Over Millbrook</h1>
  </section>

  <section class="page cover-back">
    <div class="cover-photo" role="img" aria-label="Photo of a glowing sky above dark hills"></div>
    <div class="church-info">
      <h2>CHURCH'S INFO</h2>
      <p>Lorem Ipsum is simply dummy text of the printing and typesetting industry. Lorem Ipsum has been the industry's standard dummy text ever since the 1500s</p>
    </div>
  </section>

  <section class="page spread">
    <div class="spread-photo" role="img" aria-label="Photo of a crucifix bathed in light rays inside a church"></div>
    <div class="spread-text">
      <p class="intro">God willingly created the universe, meaning he envisioned, designed, and made us.</p>
      <div class="quote-mark">&ldquo;</div>
      <p class="verse">In the beginning God created the heavens and the earth.</p>
      <div class="quote-mark">&rdquo;</div>
      <p class="reference">(Genesis 1:1)</p>
    </div>
  </section>

</body>
</html>
```